Fox & Fig honey company needs a label design.

We need a label design for a new honey company, based in the state of Florida called 'Fox & Fig". We are supplying our online customers with the highest quality of the various kinds of raw honey. Our product is honey in the oval hexagon glass jar with black lid. We would like to see designs that use black background with gold font .
In the upper part of the label is gold flying Honey Bee (profile, silhouette). The name of the brand "Fox & Fig" - Caramel font. Additional fonts are Cinzel, Source Sans Pro. Label measurements 2.6" by 3".
Label content:
Fox & Fig
RAW HONEY
wildflower
PURE & NATURAL
made by Florida Bees
foxandfigjars.com
NET WT 12oz (340g)

The final design should have eye catching, luxurious look.
Updates

Need extra days to review

Target Market(s)

Luxury

Industry/Entity Type

Food (bee products)

Font styles to use
Other font styles liked:
• caramel

Colors

Designer to choose colors to be used in the design.

Requirements
Must have
• Gold letters on black background, Drawing of a bee, flying in profile

```html
<!DOCTYPE html>
<html lang="en">
<head>
<meta charset="utf-8">
<title>Fox &amp; Fig Raw Honey Label</title>
<link rel="stylesheet" href="https://fonts.googleapis.com/css2?family=Caramel&family=Cinzel:wght@400;700&family=Source+Sans+3:wght@400;600;700&display=swap">
<style>
  :root {
    --page: #f5f5f5;
    --label-black: #000000;
    --gold: #e8cf62;
    --gold-light: #f6e08a;
    --gold-deep: #c9a63a;
    --gold-haze: rgba(232, 207, 98, 0.16);
    --ink: #111111;
    --white: #ffffff;
  }
  html, body {
    margin: 0;
    padding: 0;
    width: 1200px;
    height: 1200px;
    overflow: hidden;
    background: var(--page);
  }
  .canvas {
    position: relative;
    width: 1200px;
    height: 1200px;
    background: var(--page);
  }
  .label {
    position: absolute;
    left: 60px;
    top: 120px;
    width: 1080px;
    height: 960px;
    background: var(--label-black);
    border-radius: 42px;
    overflow: hidden;
  }
  .flight-trail {
    position: absolute;
    border-radius: 50%;
    background: radial-gradient(ellipse at center, var(--gold-haze) 0%, rgba(232, 207, 98, 0) 70%);
  }
  .flight-trail--upper-left {
    left: -40px;
    top: -20px;
    width: 340px;
    height: 320px;
  }
  .flight-trail--right {
    left: 900px;
    top: 500px;
    width: 220px;
    height: 460px;
  }
  .brand-name {
    position: absolute;
    left: 250px;
    width: 580px;
    top: 160px;
    text-align: center;
    font-family: "Caramel", cursive;
    font-weight: 400;
    font-size: 132px;
    line-height: 1;
    color: var(--gold);
  }
  .bee-illustration {
    position: absolute;
    left: 830px;
    top: 76px;
    width: 196px;
    height: 204px;
    border-radius: 50%;
    background: radial-gradient(circle at 55% 50%, rgba(232, 207, 98, 0.55) 0%, rgba(201, 166, 58, 0.3) 45%, rgba(0, 0, 0, 0) 70%);
  }
  .product-title {
    position: absolute;
    margin: 0;
    left: 0;
    width: 1080px;
    top: 358px;
    text-align: center;
    font-family: "Cinzel", serif;
    font-weight: 400;
    font-size: 112px;
    line-height: 1;
    color: var(--white);
    letter-spacing: 1px;
  }
  .product-descriptor {
    position: absolute;
    left: 0;
    width: 1080px;
    top: 478px;
    text-align: center;
    font-family: "Cinzel", serif;
    font-weight: 700;
    font-size: 40px;
    line-height: 1;
    color: var(--white);
  }
  .origin-badge {
    position: absolute;
    left: 292px;
    top: 592px;
    width: 496px;
    height: 58px;
    border-radius: 29px;
    background: linear-gradient(90deg, var(--gold-light) 0%, var(--gold) 20%, var(--gold-deep) 100%);
    display: flex;
    align-items: center;
    justify-content: center;
    font-family: "Cinzel", serif;
    font-weight: 700;
    font-size: 28px;
    letter-spacing: 2px;
    color: var(--ink);
  }
  .website {
    position: absolute;
    left: 0;
    width: 1080px;
    top: 768px;
    text-align: center;
    font-family: "Source Sans 3", sans-serif;
    font-weight: 600;
    font-size: 40px;
    letter-spacing: 1px;
    line-height: 1;
    color: var(--white);
  }
  .weight-band {
    position: absolute;
    left: 0;
    bottom: 0;
    width: 1080px;
    height: 128px;
    background: linear-gradient(90deg, var(--gold-light) 0%, #f3e07a 25%, var(--gold) 60%, var(--gold-deep) 100%);
    display: flex;
    align-items: center;
    justify-content: center;
    font-family: "Source Sans 3", sans-serif;
    font-weight: 700;
    font-size: 38px;
    letter-spacing: 2px;
    color: var(--ink);
  }
</style>
</head>
<body>
<main class="canvas">
  <section class="label">
    <div class="flight-trail flight-trail--upper-left" role="img" aria-label="Dashed gold flight path of a bee looping across the upper left corner"></div>
    <div class="flight-trail flight-trail--right" role="img" aria-label="Dashed gold flight path of a bee curving down the right edge"></div>
    <div class="brand-name">Fox &amp; Fig</div>
    <div class="bee-illustration" role="img" aria-label="Gold line drawing of a honey bee flying in profile"></div>
    <h1 class="product-title">RAW HONEY</h1>
    <div class="product-descriptor">WILD FLOWER • PURE &amp; NATURAL</div>
    <div class="origin-badge">MADE BY FLORIDA BEES</div>
    <div class="website">foxandfigjars.com</div>
    <div class="weight-band">NET WT 12OZ (340G)</div>
  </section>
</main>
</body>
</html>
```